"Fight Back" banner ad design

We have sketched the design and have images to consider including. We are looking for something striking, FIGHT BACK! with a clenched fist image, then a fading images of variance.png and hi-bill.png in the background. Tag line "Fight your water bill with your own data" optionally include "Tally Lens" brel3195 logo, KVRT Design, LLC based in San Diego CA. Pre-order now, visit https://www.pledgenest.com/brelgauge @brel3195, info@brel3195.com

"Fight your water bill with your own data"

```html
<!DOCTYPE html>
<html lang="en">
<head>
<meta charset="utf-8">
<title>Fight Back – brel3195</title>
<link rel="stylesheet" href="https://fonts.googleapis.com/css2?family=Montserrat:wght@300;400;700&family=Arimo:wght@700&display=swap">
<style>
  :root {
    --ink: #0d2a3a;
    --teal: #2f8fae;
    --brand: #2a8aa6;
    --band: #2c3e48;
    --sky: #eef6fa;
    --grid: #8f9ba0;
    --frame: #9db0b9;
    --prev: #d6eaef;
    --curr: #a2b2ba;
    --white: #ffffff;
  }
  * { margin: 0; padding: 0; box-sizing: border-box; }
  html, body { width: 1200px; height: 652px; overflow: hidden; background: var(--white); }
  .banner {
    position: relative; width: 1200px; height: 652px; overflow: hidden;
    background: radial-gradient(ellipse at 18% 30%, var(--white) 0%, var(--sky) 55%, #dcebf2 100%);
    font-family: "Montserrat", sans-serif;
  }
  .backdrop { position: absolute; inset: 0; }
  .brand-name {
    position: absolute; left: 86px; top: 304px;
    font-family: "Montserrat", sans-serif; font-weight: 700; font-size: 47px;
    color: var(--brand); letter-spacing: 0.5px;
  }
  .bill-sheet {
    position: absolute; left: 556px; top: 118px; width: 186px; height: 240px;
    background: linear-gradient(180deg, #f7f9f9 0%, #eef2f3 100%);
    border-top: 12px solid #1f5a6c; border-bottom: 10px solid #5fb7c9;
    transform: rotate(-8deg);
    box-shadow: 2px 3px 8px rgba(0,0,0,0.25);
  }
  .headline {
    position: absolute; left: 44px; top: 416px;
    font-weight: 300; font-size: 118px; line-height: 1; letter-spacing: 1px;
    color: var(--ink);
  }
  .tagline {
    position: absolute; left: 48px; top: 526px;
    font-weight: 300; font-size: 30px; letter-spacing: 0.3px;
    color: var(--teal);
  }
  .contact-band {
    position: absolute; left: 0; top: 565px; width: 1200px; height: 39px;
    background: var(--band); color: var(--white);
    font-weight: 300; font-size: 26px; line-height: 39px; padding-left: 46px;
    white-space: nowrap;
  }
  .contact-band .divider { display: inline-block; width: 1px; height: 28px; background: #7d8d96; vertical-align: middle; margin: 0 8px 0 4px; }
  .person-photo {
    position: absolute; left: 920px; top: 136px; width: 280px; height: 516px;
    background: linear-gradient(160deg, #e3c58a 0%, #d9b78a 30%, #f2d2d8 60%, #f6e3e8 100%);
    border-radius: 120px 0 0 0;
  }
</style>
</head>
<body>
<div class="banner">
  <svg class="backdrop" width="1200" height="652" viewBox="0 0 1200 652" aria-hidden="true">
    <g fill="none" stroke="#c6dde8" stroke-width="2" opacity="0.7">
      <path d="M0 420 C200 300 420 380 620 300 S1000 160 1200 220"/>
      <path d="M0 450 C220 340 440 410 640 330 S1000 200 1200 250"/>
      <path d="M900 80 C1000 140 1100 130 1200 100"/>
      <path d="M880 110 C1000 170 1100 160 1200 130"/>
    </g>
    <!-- chart -->
    <g class="usage-chart">
      <rect x="356" y="30" width="638" height="392" fill="rgba(255,255,255,0.35)" stroke="var(--frame)" stroke-width="2"/>
      <rect x="356" y="30" width="638" height="28" fill="var(--frame)"/>
      <text x="675" y="51" text-anchor="middle" font-family="Arimo, sans-serif" font-weight="700" font-size="22" fill="var(--white)">WATER USE IN HCF (Hundred Cubic Feet)</text>
      <rect x="522" y="64" width="18" height="17" fill="var(--prev)" stroke="var(--grid)"/>
      <text x="557" y="80" font-family="Arimo, sans-serif" font-weight="700" font-size="15" fill="#8d979c">Previous Year</text>
      <rect x="688" y="64" width="18" height="17" fill="var(--curr)"/>
      <text x="721" y="80" font-family="Arimo, sans-serif" font-weight="700" font-size="15" fill="#8d979c">Current Year</text>
      <g stroke="var(--grid)" stroke-width="1.6">
        <line x1="398" y1="92" x2="984" y2="92"/><line x1="398" y1="112" x2="984" y2="112"/>
        <line x1="398" y1="132" x2="984" y2="132"/><line x1="398" y1="153" x2="984" y2="153"/>
        <line x1="398" y1="173" x2="984" y2="173"/><line x1="398" y1="193" x2="984" y2="193"/>
        <line x1="398" y1="213" x2="984" y2="213"/><line x1="398" y1="234" x2="984" y2="234"/>
        <line x1="398" y1="254" x2="984" y2="254"/><line x1="398" y1="274" x2="984" y2="274"/>
        <line x1="398" y1="294" x2="984" y2="294"/><line x1="398" y1="315" x2="984" y2="315"/>
        <line x1="398" y1="335" x2="984" y2="335"/><line x1="398" y1="355" x2="984" y2="355"/>
        <line x1="398" y1="375" x2="984" y2="375"/><line x1="398" y1="396" x2="984" y2="396"/>
        <line x1="398" y1="416" x2="984" y2="416"/>
      </g>
      <g font-family="Arimo, sans-serif" font-size="15" fill="#7d878c" text-anchor="end">
        <text x="389" y="97">80</text><text x="389" y="117">75</text><text x="389" y="137">70</text>
        <text x="389" y="158">65</text><text x="389" y="178">60</text><text x="389" y="198">55</text>
        <text x="389" y="218">50</text><text x="389" y="239">45</text><text x="389" y="259">40</text>
        <text x="389" y="279">35</text><text x="389" y="299">30</text><text x="389" y="320">25</text>
        <text x="389" y="340">20</text><text x="389" y="360">15</text><text x="389" y="380">10</text>
        <text x="389" y="401">5</text><text x="389" y="421">0</text>
      </g>
      <g fill="var(--prev)" stroke="#c3dbe2">
        <rect x="442" y="307" width="20" height="109"/>
        <rect x="542" y="278" width="20" height="138"/>
        <rect x="642" y="351" width="20" height="65"/>
        <rect x="742" y="299" width="20" height="117"/>
        <rect x="840" y="315" width="20" height="101"/>
        <rect x="940" y="315" width="20" height="101"/>
      </g>
      <g fill="var(--curr)">
        <rect x="468" y="323" width="20" height="93"/>
        <rect x="566" y="335" width="20" height="81"/>
        <rect x="666" y="351" width="20" height="65"/>
        <rect x="766" y="96" width="20" height="320"/>
        <rect x="864" y="145" width="20" height="271"/>
        <rect x="964" y="124" width="20" height="292"/>
      </g>
    </g>
  </svg>

  <div class="brand-name">brel3195</div>

  <div class="bill-sheet" role="img" aria-label="Water bill statement listing fees, tiered water charges and a total due"></div>

  <div class="person-photo" role="img" aria-label="Photo of a surprised woman reading her water bill"></div>

  <h1 class="headline">FIGHT BACK!</h1>
  <p class="tagline">FIGHT YOUR WATER BILL WITH YOUR OWN DATA</p>
  <div class="contact-band">visit https://www.pledgenest.com/brelgauge @brel3195,<span class="divider"></span>info@brel3195.com</div>
</div>
</body>
</html>
```